Elegant, High End Integrated Wellness Healthcare Practice

We need a brochure designed for an integrated mind-body wellness healthcare practice (www.larkfieldcare.com) . This brochure will be used when we cold call prospects (physicians to refer to our office, and potential consumers to utilize our services). Our practice is geographically located in the middle Tennessee USA region, although we have plans to become an international company as many of our offerings can be accessed anywhere in the world. Ultimately our goal is to have this brochure used as a leave-behind in an effort to introduce our integrated offerings to increase market share. The final product brochure should be both elegant and serious, with clean lines but also convey warmth and trust, as individuals who are coming for our services have usually struggled with their health for a significant amount of time before finding our practice.
Updates

The design brief was very specific about providing a high-end science-based 2-page brochure (not flier). Several designs submitted were fliers. The other designs were heavy on yoga or "woo woo" non-science-based looking pictures. This is a flier to appeal to physicians and other healthcare providers. Therefore the design must speak science and evidence-based methods of mind and body wellness care. I would also like to appeal to the other designers I paid extra for their submissions and who have indicated they will "respond in the coming days."

```html
<!DOCTYPE html>
<html lang="en">
<head>
<meta charset="utf-8">
<title>Larkfield Care – Brochure</title>
<link href="https://fonts.googleapis.com/css2?family=Alike&family=Mulish:wght@400&display=swap" rel="stylesheet">
<style>
  :root{
    --stage:#404043;
    --leaf:#75aa3b;
    --leaf-deep:#2f4d18;
    --rule-dark:#3d6021;
    --ink-dark:#111111;
    --ink-soft:#1c1c1c;
    --paper:#f0fbe6;
    --text:#1e1e1e;
    --white:#f4f4f4;
    --serif:'Alike', Georgia, serif;
    --sans:'Mulish', Arial, sans-serif;
  }
  *{margin:0;padding:0;box-sizing:border-box}
  html,body{width:1200px;height:848px;overflow:hidden;background:var(--stage)}
  .canvas{position:relative;width:1200px;height:848px}
  .page{position:absolute;top:56px;width:506px;height:715px;overflow:hidden}
  .page--cover{left:72px;background:var(--ink-dark)}
  .page--inside{left:624px;background:var(--paper)}
  .abs{position:absolute}
  .cover-shapes{position:absolute;inset:0}
  .cover-title{left:30px;top:20px;font:31px/40px var(--serif);font-weight:400;color:var(--ink-dark)}
  .cover-call{left:284px;top:20px;font:28px/34px var(--serif);color:var(--white)}
  .brand-cover{left:116px;top:390px;font:34px/42px var(--serif);color:var(--leaf-deep);letter-spacing:1px}
  .services{left:0;top:497px;width:236px;list-style:none}
  .services li{position:relative;height:41px;padding-left:37px;font:16px/41px var(--serif);color:var(--white);border-bottom:1px solid var(--rule-dark)}
  .services li:last-child{border-bottom:none}
  .services li::before{content:"";position:absolute;left:15px;top:16px;width:10px;height:10px;border-radius:50%;background:var(--leaf)}
  .info{font:17px/23.5px var(--serif);color:var(--white)}
  .info--address{left:328px;top:532px}
  .info--hours{left:331px;top:624px}
  .icon{position:absolute}
  .brand-inside{left:79px;top:20px;font:18px/22px var(--serif);color:var(--leaf-deep);letter-spacing:.5px}
  .inside-call{left:332px;top:14px;font:24px/28px var(--serif);color:var(--text)}
  .section-title{font:21px/26px var(--serif);font-weight:400;color:var(--text)}
  .section-body{font:13px/16px var(--sans);color:var(--text)}
  .photo{position:absolute;border-radius:50%}
  .rule{position:absolute;height:2px;background:var(--leaf)}
</style>
</head>
<body>
<div class="canvas">

  <section class="page page--cover">
    <svg class="cover-shapes" width="506" height="715" viewBox="0 0 506 715">
      <path d="M0 0H506V255L231 300L95 320C50 322 10 295 0 258Z" fill="var(--leaf)"/>
      <circle cx="452" cy="678" r="226" fill="var(--ink-soft)"/>
    </svg>
    <div class="photo" role="img" aria-label="Hand holding a glowing light bulb with a brain inside" style="left:220px;top:105px;width:272px;height:272px;background:radial-gradient(circle at 50% 40%,#d8b36a 0%,#6b5a45 22%,#3c3835 55%,#4a4744 100%)"></div>
    <h1 class="abs cover-title">What We Do at<br>Larkfield<br>Care in<br>Ashbury Glen,<br>TN</h1>
    <div class="abs cover-call">Call Us<br>(555) 201 - 0142</div>

    <svg class="icon" style="left:26px;top:379px" width="84" height="84"><circle cx="42" cy="42" r="40" fill="var(--leaf-deep)"/></svg>
    <div class="abs brand-cover">Larkfield<br>Care</div>

    <ul class="abs services">
      <li>An Integrative Approach</li>
      <li>Personalized Care</li>
      <li>Innovative Treatments</li>
      <li>Root Cause Resolution</li>
      <li>Co-Creating Health</li>
    </ul>

    <svg class="icon" style="left:288px;top:532px" width="26" height="30" viewBox="0 0 26 30" fill="none" stroke="var(--white)" stroke-width="1.8">
      <path d="M13 23C8 17 5 13 5 9.5a8 8 0 0116 0C21 13 18 17 13 23Z"/><circle cx="13" cy="9.5" r="3"/><path d="M7 22c-3 1-4 2-4 3 0 2 4.5 3 10 3s10-1 10-3c0-1-1-2-4-3"/>
    </svg>
    <div class="abs info info--address">480 Alder Run Dr.<br>Ashbury Glen, TN<br>37990</div>

    <svg class="icon" style="left:285px;top:622px" width="28" height="28" viewBox="0 0 28 28" fill="none" stroke="var(--white)" stroke-width="1.8">
      <circle cx="14" cy="14" r="12"/><path d="M14 7v7l4 4"/>
    </svg>
    <div class="abs info info--hours">Operating Hours<br>Monday - Friday:<br>8am - 7pm</div>
  </section>

  <section class="page page--inside">
    <svg class="icon" style="left:22px;top:16px" width="52" height="52"><circle cx="26" cy="26" r="25" fill="var(--leaf-deep)"/></svg>
    <div class="abs brand-inside">Larkfield<br>Care</div>

    <svg class="icon" style="left:283px;top:25px" width="40" height="40" viewBox="0 0 40 40">
      <circle cx="20" cy="20" r="20" fill="var(--leaf)"/>
      <path d="M14 11c1-1 2-1 3 0l2 3c.5 1 .3 2-.5 2.6l-1 .8c1 2.3 2.8 4.1 5 5l.8-1c.6-.8 1.6-1 2.5-.5l3 2c1 .7 1 2 0 3l-1.5 1.5c-1 1-3 1.3-5 .3-4.5-2.2-8-5.7-10-10-.9-2-.6-4 .4-5Z" fill="#fff"/>
    </svg>
    <div class="abs inside-call">Call Us<br>(555) 201 - 0142</div>

    <h2 class="abs section-title" style="left:29px;top:92px">An Integrative Approach</h2>
    <p class="abs section-body" style="left:29px;top:127px;width:302px">Join us in our mission to change healthcare as we know it. Guided step-by-step by our care team, well embark on an integrative approach to cover more of the issues we face across the lifespan. Dedicated Attention</p>
    <div class="photo" role="img" aria-label="Hand stacking wooden blocks printed with planning icons" style="left:352px;top:92px;width:113px;height:113px;background:radial-gradient(circle at 60% 40%,#6b93a8,#3f6f86 70%,#c9cfd2 100%)"></div>
    <div class="rule" style="left:0;top:224px;width:457px"></div>

    <div class="photo" role="img" aria-label="Woman blowing on a dandelion in a sunlit field" style="left:25px;top:237px;width:113px;height:113px;background:radial-gradient(circle at 70% 40%,#e6d3a4,#8c6a45 55%,#4a3424 100%)"></div>
    <h2 class="abs section-title" style="left:162px;top:240px">Personalized Care</h2>
    <p class="abs section-body" style="left:162px;top:274px;width:280px">This is no “one-size-fits-all” when it comes to giving yourself the best care. Everyone is biologically unique, and as we age, we have different needs and requirements.</p>
    <div class="rule" style="left:44px;top:369px;width:462px"></div>

    <h2 class="abs section-title" style="left:27px;top:385px">Innovative Treatments</h2>
    <p class="abs section-body" style="left:27px;top:414px;width:320px">Did you know that it takes on average 17 years for clinical breakthroughs to make their way into your conventional doctor’s office? That means many health care practitioners are dispensing outdated advice and not using the best evaluation techniques for your particular symptoms and circumstances.</p>
    <div class="photo" role="img" aria-label="Digital circuit-pattern head in glowing blue" style="left:359px;top:394px;width:113px;height:113px;background:radial-gradient(circle at 45% 45%,#2aa7c9,#0b5f86 55%,#062c4a 100%)"></div>
    <div class="rule" style="left:0;top:528px;width:457px"></div>

    <div class="photo" role="img" aria-label="Woman breathing fresh air among green trees" style="left:25px;top:551px;width:113px;height:113px;background:radial-gradient(circle at 40% 40%,#b7d66a,#5f8f2c 60%,#2f5418 100%)"></div>
    <h2 class="abs section-title" style="left:162px;top:542px">Co-Creating Health</h2>
    <p class="abs section-body" style="left:162px;top:573px;width:322px">Changing your lifestyle may seem daunting, but we also equip you with mindset tools &amp; mentorship to overcome life habits that are an impediment to optimal wellness. We make the prospect of getting healthy “enjoyable.” We have a wide range of tools to support you during your body &amp; mind health transformation and help build resilience and regain energy.</p>
  </section>

</div>
</body>
</html>
```